Redesign our business card for more impact

We want to completely replace the back design of our card, and refresh or even change the front entirely. We are happy with our black Q7 logo and do not want to change it.
Our company address changed too. It is now 58 Corvallen, Irvine, CA 92741
Updates

It was reported by Sketch Harbor email today that the uploaded files didnt upload. I am trying again.

Target Market(s)

Architects and Building Owners (People making multi-million dollar decisions)

Industry/Entity Type

Consulting Engineering

Contact Information for Business Card

Contact info on the front. "wallpaper" design on back with tag line on the back "Engineering Your Future"

Font styles to use
Sans Serif

Requirements
Must have
• A vivid, modern, impactful ...but tasteful back of card design. It should communicate our premier status, but grab attention as innovative. DESIGN SHOULD BE ELEGANT AND NOT TOO BUSY.
Nice to have
• Repeating pattern, multi-color, something creative...
Should not have
• Anything that looks too playful or that we are not serious professionals. It should also not be too boring or conservative.

```html
<!DOCTYPE html>
<html lang="en">
<head>
<meta charset="utf-8">
<title>Q7 Engineering – Business Card</title>
<link rel="stylesheet" href="https://fonts.googleapis.com/css2?family=Jost:wght@400;500;700&display=swap">
<style>
  :root {
    --ink: #141414;
    --page: #ecebef;
    --foil-pink: #f3d3f2;
    --foil-lilac: #cbb8f5;
    --foil-sky: #a6e6fb;
    --foil-blue: #8aa5e4;
    --foil-periwinkle: #a9b4f0;
  }
  * { margin: 0; padding: 0; box-sizing: border-box; }
  html, body {
    width: 1200px; height: 900px; overflow: hidden;
    background: var(--page);
    font-family: "Jost", "Futura", sans-serif;
    color: var(--ink);
  }
  .card {
    position: absolute; left: 100px; top: 141px;
    width: 1000px; height: 618px;
    overflow: hidden;
    box-shadow: 0 18px 40px rgba(40, 40, 70, 0.18);
    background:
      radial-gradient(ellipse 320px 260px at 8% 10%, var(--foil-pink), transparent 70%),
      radial-gradient(ellipse 360px 280px at 30% 30%, var(--foil-lilac), transparent 72%),
      radial-gradient(ellipse 380px 300px at 72% 18%, var(--foil-sky), transparent 70%),
      radial-gradient(ellipse 320px 260px at 80% 65%, var(--foil-blue), transparent 72%),
      radial-gradient(ellipse 300px 220px at 42% 90%, var(--foil-pink), transparent 70%),
      radial-gradient(ellipse 320px 260px at 6% 80%, var(--foil-blue), transparent 72%),
      var(--foil-periwinkle);
  }
  .centered { position: absolute; left: 0; width: 100%; text-align: center; }
  .brand-name {
    top: 10px; font-size: 200px; font-weight: 700; line-height: 1; letter-spacing: -6px;
  }
  .tagline { top: 222px; font-size: 23px; font-weight: 400; letter-spacing: 0.5px; }
  .person-name { top: 276px; font-size: 37px; font-weight: 700; letter-spacing: 0.5px; }
  .credentials { top: 322px; font-size: 27px; }
  .role { top: 362px; font-size: 27px; }
  .divider {
    position: absolute; left: 461px; width: 79px; height: 1.5px; background: var(--ink);
  }
  .divider.upper { top: 414px; }
  .divider.lower { top: 470px; }
  .address { top: 420px; font-size: 28px; letter-spacing: 0.6px; }
  .contact-item {
    position: absolute; top: 490px; transform: translateX(-50%);
    display: flex; flex-direction: column; align-items: center;
    white-space: nowrap; font-size: 27px; letter-spacing: 0.6px;
  }
  .contact-icon {
    width: 60px; height: 60px; border: 1.5px solid var(--ink); border-radius: 50%;
    display: flex; align-items: center; justify-content: center; margin-bottom: 2px;
    margin-left: var(--icon-shift, 0);
  }
  .contact-icon svg { width: 30px; height: 30px; }
  .contact-phone { left: 171px; --icon-shift: -32px; }
  .contact-email { left: 550px; --icon-shift: -78px; }
  .contact-web { left: 856px; --icon-shift: -16px; }
</style>
</head>
<body>
  <main class="card">
    <div class="centered brand-name">Q7</div>
    <div class="centered tagline">Engineering Your Future</div>
    <div class="centered person-name">DANIEL WHITCOMBE, PE</div>
    <div class="centered credentials">HFDP, LEED AP</div>
    <div class="centered role">CEO/Principal</div>
    <div class="divider upper"></div>
    <div class="centered address">58 Corvallen, Irvine, CA 92741</div>
    <div class="divider lower"></div>

    <div class="contact-item contact-phone">
      <span class="contact-icon">
        <svg viewBox="0 0 24 24" aria-hidden="true"><path fill="#141414" d="M6.6 10.8a15.1 15.1 0 0 0 6.6 6.6l2.2-2.2a1 1 0 0 1 1-.25 11.4 11.4 0 0 0 3.6.57 1 1 0 0 1 1 1V20a1 1 0 0 1-1 1A17 17 0 0 1 3 4a1 1 0 0 1 1-1h3.5a1 1 0 0 1 1 1c0 1.25.2 2.45.57 3.6a1 1 0 0 1-.25 1z"/><path fill="none" stroke="#141414" stroke-width="1.6" stroke-linecap="round" d="M14 3.5a7 7 0 0 1 6.5 6.5M14 7a3.5 3.5 0 0 1 3 3"/></svg>
      </span>
      (626) 555-0184
    </div>

    <div class="contact-item contact-email">
      <span class="contact-icon">
        <svg viewBox="0 0 24 24" aria-hidden="true"><rect x="2.5" y="5" width="19" height="14" fill="#141414"/><path fill="none" stroke="#f0e6fb" stroke-width="1.4" d="M2.5 5.5 12 13l9.5-7.5M2.5 19l7-6.5M21.5 19l-7-6.5"/></svg>
      </span>
      daniel.whitcombe@q7eng.com
    </div>

    <div class="contact-item contact-web">
      <span class="contact-icon">
        <svg viewBox="0 0 24 24" aria-hidden="true"><g fill="none" stroke="#141414" stroke-width="1.8"><circle cx="12" cy="12" r="9.5"/><ellipse cx="12" cy="12" rx="4.2" ry="9.5"/><path d="M2.5 12h19M4 7.5h16M4 16.5h16M12 2.5v19"/></g></svg>
      </span>
      q7eng.com
    </div>
  </main>
</body>
</html>
```